Looking for a cool & simple business-card-design for digital agency

Hi!

We are a web agency that offers Reputation Management, Zorvik & Seo Services and software development. We like cool things, we like innovative styles.

We have uploaded our logo.

Project Deadline Extended Reason: Client does not want any designs with the colorful logo. Please send us submissions ONLY with the blac and white logo. What the client would like to see:1) Back of the card: is a silver logo on a black background2) front of the card with all the data, please use white background and black logo thank you Added Friday, May 8, 2015

Software

```html
<!DOCTYPE html>
<html lang="de">
<head>
<meta charset="utf-8">
<title>Kelvora AG – Visitenkarte</title>
<link rel="stylesheet" href="https://fonts.googleapis.com/css2?family=Josefin+Sans:wght@300;400;600&display=swap">
<style>
  :root {
    --backdrop: #c9c9c9;
    --card-front: #ffffff;
    --card-back: #1e1e1e;
    --ink: #1b1b1b;
    --ink-soft: #4a4a4a;
    --rule: #c4c4c4;
    --silver: #c2c2c2;
    --front-deco: #f1f1f1;
    --back-deco: #262626;
    --shadow: rgba(0, 0, 0, 0.35);
  }
  * { margin: 0; padding: 0; box-sizing: border-box; }
  html, body {
    width: 1200px;
    height: 1200px;
    overflow: hidden;
    background: var(--backdrop);
    font-family: "Josefin Sans", "Helvetica Neue", Arial, sans-serif;
  }
  .canvas { position: relative; width: 1200px; height: 1200px; }

  .card {
    position: absolute;
    left: 177px;
    width: 848px;
    height: 495px;
    overflow: hidden;
    box-shadow: 4px 6px 10px var(--shadow);
  }
  .card--front { top: 75px; background: var(--card-front); color: var(--ink); }
  .card--back { top: 630px; background: var(--card-back); color: var(--silver); }

  .card__deco {
    position: absolute;
    top: 40px;
    right: 90px;
    width: 330px;
    height: 420px;
    border-radius: 24px;
  }
  .card--front .card__deco { background: var(--front-deco); }
  .card--back .card__deco { background: var(--back-deco); }

  .brand {
    position: absolute;
    display: flex;
    align-items: center;
    gap: 18px;
  }
  .brand__mark {
    width: 46px;
    height: 46px;
    background: currentColor;
  }
  .brand__text { display: flex; flex-direction: column; }
  .brand__name {
    font-weight: 600;
    font-size: 50px;
    line-height: 1;
    letter-spacing: 1px;
  }
  .brand__tagline {
    font-weight: 400;
    font-size: 25px;
    letter-spacing: 5.5px;
    margin-top: 6px;
  }
  .card--front .brand { left: 113px; top: 68px; color: var(--ink); }
  .card--back .brand { left: 100px; top: 210px; color: var(--silver); }

  .details {
    position: absolute;
    left: 73px;
    top: 222px;
    font-weight: 300;
    font-size: 22px;
    line-height: 33px;
    color: var(--ink-soft);
  }
  .details__rule {
    width: 320px;
    height: 1px;
    background: var(--rule);
    margin: 14px 0 18px;
  }
  .details__address { margin-bottom: 12px; }
</style>
</head>
<body>
<main class="canvas">

  <section class="card card--front" aria-label="Kartenvorderseite">
    <div class="card__deco" aria-hidden="true"></div>
    <div class="brand">
      <span class="brand__mark" aria-hidden="true"></span>
      <div class="brand__text">
        <span class="brand__name">Kelvora AG</span>
        <span class="brand__tagline">DIGITALE STRATEGIEN</span>
      </div>
    </div>
    <div class="details">
      <p class="details__services">Reputation Management,<br>Zorvik &amp; Seo Services &amp; software development</p>
      <div class="details__rule"></div>
      <p class="details__address">Dummy city Dummy country<br>Dummy land</p>
      <p class="details__phone">555.555.5555</p>
      <p class="details__web">lena.marsh@mailbox.net | www.website.com</p>
    </div>
  </section>

  <section class="card card--back" aria-label="Kartenrückseite">
    <div class="card__deco" aria-hidden="true"></div>
    <div class="brand">
      <span class="brand__mark" aria-hidden="true"></span>
      <div class="brand__text">
        <span class="brand__name">Kelvora AG</span>
        <span class="brand__tagline">DIGITALE STRATEGIEN</span>
      </div>
    </div>
  </section>

</main>
</body>
</html>
```